Willow Current Mind Studio

I need a brain fitness website that is on the WordPress platform. It needs to feel friendly and relaxing. We are not a physical health gym, but a brain health coaching facility. I can produce hundreds of professional photos. It can be one long page or five short pages.

Industry/Entity Type

Health And Wellness

```html
<!DOCTYPE html>
<html lang="en">
<head>
<meta charset="utf-8">
<title>Willow Current Mind Studio</title>
<link href="https://fonts.googleapis.com/css2?family=Lato:ital,wght@0,400;0,700;0,900;1,400&display=swap" rel="stylesheet">
<style>
:root{
  --maroon:#8e1a4e;
  --navy:#1b4a62;
  --blue:#2b7db8;
  --sky:#2aa3e0;
  --text:#333;
  --light:#f3f3f3;
  --grad:linear-gradient(90deg,#8a1f4f 0%,#5c3c70 45%,#2b7db8 100%);
}
*{box-sizing:border-box;margin:0;padding:0}
html,body{width:1200px;height:3509px;overflow:hidden}
body{font-family:'Lato',sans-serif;color:var(--text);background:#fff;position:relative}
.abs{position:absolute}
.btn{position:absolute;display:flex;align-items:center;justify-content:center;background:var(--navy);color:#fff;font-weight:700;font-size:15px;letter-spacing:.5px;border-radius:26px;text-transform:uppercase}
.mark{width:42px;height:42px;border-radius:50%;border:2px solid #b77ea0;background:#f6eef3;position:absolute}
.heading{position:absolute;left:0;width:1200px;text-align:center;color:var(--maroon);font-weight:900;font-size:29px;letter-spacing:.5px;text-transform:uppercase}

/* header */
.header{position:absolute;top:0;left:0;width:1200px;height:117px;background:#fff}
.brand{position:absolute;left:72px;top:18px;width:160px;text-align:center;color:var(--maroon);font-weight:700;font-size:13px;line-height:15px}
.brand .dot{display:block;margin:0 auto 6px;width:40px;height:40px;border-radius:50%;background:#e9d6e1}
.nav{position:absolute;left:340px;top:51px;display:flex;gap:34px;font-size:14px;font-weight:700;color:#222}
.nav .active{color:var(--maroon)}
.header-cta{left:908px;top:37px;width:218px;height:46px;background:var(--grad);font-size:14px}

/* hero */
.hero{position:absolute;top:117px;left:0;width:1200px;height:546px;background:radial-gradient(ellipse at 50% 45%,#d9c9c4 0%,#c9c6c8 35%,#9fa4aa 75%,#7d8288 100%)}
.hero-title{position:absolute;top:178px;width:1200px;text-align:center;color:var(--maroon);font-weight:900;font-size:49px;letter-spacing:1px}
.hero-sub{position:absolute;top:230px;width:1200px;text-align:center;color:#fff;font-weight:900;font-size:37px;letter-spacing:1px}
.hero-cta{left:492px;top:295px;width:216px;height:44px;background:var(--maroon);font-size:13px}
.dots{position:absolute;top:500px;left:565px;display:flex;gap:8px}
.dots span{width:10px;height:10px;border-radius:50%;background:#fff}
.dots span.on{background:var(--blue)}

/* welcome */
.welcome-text{position:absolute;top:798px;left:150px;width:900px;text-align:center;font-size:16.5px;line-height:29.5px;color:#333}

/* services */
.services{position:absolute;top:1046px;left:0;width:1200px;height:448px;background:var(--light)}
.services-intro{position:absolute;left:70px;top:0;width:250px;text-align:center}
.services-intro h2{position:absolute;top:164px;width:250px;color:var(--maroon);font-weight:900;font-size:29px}
.services-intro p{position:absolute;top:206px;width:250px;font-size:14.5px;line-height:24px}
.services-photo{position:absolute;left:690px;top:0;width:510px;height:448px;background:linear-gradient(120deg,#6b6f78 0%,#9a9da3 45%,#d8d4d0 100%)}
.services-panel{position:absolute;left:343px;top:46px;width:514px;height:356px;background:var(--grad);color:#fff}
.service{position:absolute;left:24px;width:470px;height:80px}
.service .icon{position:absolute;left:0;top:0;width:70px;height:70px;border:2px solid #fff;border-radius:50%;display:flex;align-items:center;justify-content:center}
.service h3{position:absolute;left:100px;top:0;font-size:19px;font-weight:700}
.service p{position:absolute;left:100px;top:28px;width:370px;font-size:14px;line-height:22px}

/* blog */
.blog-img{position:absolute;top:1660px;height:191px;background:linear-gradient(135deg,#c9b9a6 0%,#e4ddd4 55%,#9a8d80 100%)}
.blog-title{position:absolute;top:1864px;width:335px;color:var(--blue);font-size:26px;line-height:32px}
.blog-text{position:absolute;top:1935px;width:335px;font-size:16.5px;line-height:29px}

/* testimonial */
.testimonials{position:absolute;top:2175px;left:0;width:1200px;height:385px;background:var(--grad)}
.testimonials h2{position:absolute;top:52px;width:1200px;text-align:center;color:#fff;font-weight:700;font-size:29px}
.patient-photo{position:absolute;left:165px;top:113px;width:201px;height:196px;border:4px solid #fff;background:linear-gradient(160deg,#e9e7e5 0%,#cfc9c3 60%,#b9b2aa 100%)}
.quote-text{position:absolute;left:462px;top:115px;width:590px;color:#fff;font-style:italic;font-size:16px;line-height:29.5px}
.quote-name{position:absolute;left:462px;top:275px;color:var(--sky);font-size:15px;font-weight:700}

/* subscribe */
.sub-text{position:absolute;top:2657px;width:1200px;text-align:center;font-size:15px}
.subscribe{position:absolute;left:248px;top:2703px;width:702px;height:52px;border:1px solid #d8d8d8;border-radius:26px;background:#fff;box-shadow:0 1px 4px rgba(0,0,0,.12)}
.subscribe span{position:absolute;left:55px;top:16px;font-size:15px;color:#333}
.subscribe .btn{left:560px;top:5px;width:138px;height:42px;font-size:15px}

/* contact */
.contact{position:absolute;top:2815px;left:0;width:1200px;height:452px;background:var(--light)}
.map{position:absolute;left:0;top:0;width:510px;height:452px;background:linear-gradient(135deg,#e8eadf 0%,#d7e6c9 45%,#c9dceb 100%)}
.form-panel{position:absolute;left:343px;top:50px;width:514px;height:356px;background:var(--grad)}
.form-panel h2{position:absolute;top:22px;width:514px;text-align:center;color:#fff;font-size:29px;font-weight:700;letter-spacing:.5px}
.field{position:absolute;height:40px;background:#fff;border-radius:20px;font-size:12.5px;font-weight:700;color:#333;padding:13px 20px}
.field.msg{border-radius:20px;height:84px}
.submit{left:168px;top:294px;width:178px;height:46px;background:#2aa3e0;font-size:15px}
.contact-info{position:absolute;left:890px;top:0;width:230px;text-align:center}
.contact-info h2{position:absolute;top:146px;width:230px;color:var(--maroon);font-weight:900;font-size:27px}
.contact-info .name{position:absolute;top:188px;width:230px;color:var(--blue);font-weight:700;font-size:17px}
.contact-info .addr{position:absolute;top:217px;width:230px;font-size:15px;line-height:26px}
.info-line{position:absolute;left:10px;width:230px;display:flex;align-items:center;justify-content:center;gap:12px;font-size:15px}

/* footer */
.footer-brand{position:absolute;top:3304px;left:500px;width:200px;text-align:center;color:var(--maroon);font-weight:700;font-size:13px;line-height:15px}
.footer-brand .dot{display:block;margin:0 auto 6px;width:40px;height:40px;border-radius:50%;background:#e9d6e1}
.copy{position:absolute;top:3406px;width:1200px;text-align:center;font-size:13px}
.socials{position:absolute;top:3435px;left:490px;display:flex;gap:22px}
.socials span{width:26px;height:26px;border-radius:50%;background:#444}
</style>
</head>
<body>

<header class="header">
  <div class="brand"><span class="dot"></span>WILLOW CURRENT<br>MIND STUDIO</div>
  <nav class="nav">
    <span class="active">HOME</span><span>ABOUT US</span><span>SERVICES</span><span>BLOG</span><span>TESTIMONIAL</span><span>CONTACT US</span>
  </nav>
  <div class="btn header-cta">Make an Appointment</div>
</header>

<section class="hero" role="img" aria-label="Photo of a doctor's hands holding a model of a human brain">
  <div class="hero-title">WILLOW CURRENT</div>
  <div class="hero-sub">MIND STUDIO</div>
  <div class="btn hero-cta">Make an Appointment</div>
  <div class="dots"><span class="on"></span><span></span><span></span><span></span></div>
</section>

<section>
  <div class="mark" style="left:579px;top:697px"></div>
  <h2 class="heading" style="top:748px">Welcome to our website</h2>
  <p class="welcome-text">Aliquam molestie, mi et imperdiet euismod, dui purus auctor tellus, et interdum lacus lectus et ante.<br>Sed accumsan sollicitudin sapien, sit amet adipiscing turpis gravida ac. In congue, neque ac lobortis volutpat, libero mauris varius mi, vitae suscipit ipsum ligula vitae risus. Duis aliquam nibh a dui iaculis viverra id a velit.<br>Vivamus egestas risus in magna varius commodo. Sed semper viverra egestas.</p>
  <div class="btn" style="left:510px;top:946px;width:180px;height:47px">Read More</div>
</section>

<section class="services">
  <div class="services-intro">
    <div class="mark" style="left:104px;top:110px"></div>
    <h2>OUR SERVICES</h2>
    <p>Aliquam molestie, mi et imperdiet euismod, dui purus auctor tellus, et interdum lacus lectus et ante.</p>
    <div class="btn" style="left:35px;top:310px;width:180px;height:47px">Read More</div>
  </div>
  <div class="services-photo" role="img" aria-label="Photo of a coach taking notes on a clipboard"></div>
  <div class="services-panel">
    <div class="service" style="top:36px">
      <div class="icon"><svg width="34" height="34" viewBox="0 0 34 34" fill="none" stroke="#fff" stroke-width="2"><rect x="5" y="5" width="24" height="24" rx="4"/><path d="M11 17h12M17 11v12"/></svg></div>
      <h3>Brain Health Coaching</h3>
      <p>Aliquam molestie, mi et imperdiet euismod, dui purus auctor tellus, et interdum lacus lectus et ante.</p>
    </div>
    <div class="service" style="top:141px">
      <div class="icon"><svg width="34" height="34" viewBox="0 0 34 34" fill="none" stroke="#fff" stroke-width="2"><circle cx="17" cy="11" r="6"/><path d="M6 30c0-7 5-11 11-11s11 4 11 11z"/></svg></div>
      <h3>Group Coaching</h3>
      <p>Aliquam molestie, mi et imperdiet euismod, dui purus auctor tellus, et interdum lacus lectus et ante.</p>
    </div>
    <div class="service" style="top:246px">
      <div class="icon"><svg width="40" height="34" viewBox="0 0 40 34" fill="none" stroke="#fff" stroke-width="2"><circle cx="20" cy="10" r="5"/><circle cx="8" cy="14" r="4"/><circle cx="32" cy="14" r="4"/><path d="M11 30c0-6 4-10 9-10s9 4 9 10zM1 30c0-5 3-8 7-8M39 30c0-5-3-8-7-8"/></svg></div>
      <h3>Individual Coaching</h3>
      <p>Aliquam molestie, mi et imperdiet euismod, dui purus auctor tellus, et interdum lacus lectus et ante.</p>
    </div>
  </div>
</section>

<section>
  <div class="mark" style="left:579px;top:1548px"></div>
  <h2 class="heading" style="top:1602px">Blog Posts</h2>
  <div class="blog-img" style="left:75px;width:331px" role="img" aria-label="Photo of a support group sitting in a circle"></div>
  <div class="blog-img" style="left:433px;width:331px" role="img" aria-label="Photo of a counselling session on a sofa"></div>
  <div class="blog-img" style="left:795px;width:331px" role="img" aria-label="Photo of a therapist talking with a client"></div>
  <h3 class="blog-title" style="left:75px">Vestibulum ante ipsum primis in faucibus orci luctus</h3>
  <h3 class="blog-title" style="left:433px">Vestibulum ante ipsum primis in faucibus orci luctus</h3>
  <h3 class="blog-title" style="left:795px">Vestibulum ante ipsum primis in faucibus orci luctus</h3>
  <p class="blog-text" style="left:75px">Aliquam molestie, mi et imperdiet euismod, dui purus auctor tellus, et interdum lacus lectus et ante.</p>
  <p class="blog-text" style="left:433px">Aliquam molestie, mi et imperdiet euismod, dui purus auctor tellus, et interdum lacus lectus et ante.</p>
  <p class="blog-text" style="left:795px">Aliquam molestie, mi et imperdiet euismod, dui purus auctor tellus, et interdum lacus lectus et ante.</p>
  <div class="btn" style="left:510px;top:2072px;width:180px;height:47px">View All</div>
</section>

<section class="testimonials">
  <h2>HAPPY PATIENTS</h2>
  <svg class="abs" style="left:95px;top:198px" width="22" height="34" viewBox="0 0 22 34"><path d="M18 3L5 17l13 14" fill="none" stroke="#fff" stroke-width="4"/></svg>
  <svg class="abs" style="left:1082px;top:198px" width="22" height="34" viewBox="0 0 22 34"><path d="M4 3l13 14L4 31" fill="none" stroke="#fff" stroke-width="4"/></svg>
  <div class="patient-photo" role="img" aria-label="Portrait photo of a smiling patient"></div>
  <svg class="abs" style="left:403px;top:122px" width="40" height="32" viewBox="0 0 40 32"><path d="M2 30V16C2 8 7 3 16 2v6c-5 1-7 4-7 8h7v14zM23 30V16c0-8 5-13 14-14v6c-5 1-7 4-7 8h7v14z" fill="#2aa3e0"/></svg>
  <p class="quote-text">Aliquam molestie, mi et imperdiet euismod, dui purus auctor tellus, et interdum lacus lectus et ante.&nbsp; Sed accumsan sollicitudin sapien, sit amet adipiscing turpis gravida ac. In congue, neque ac lobortis volutpat, libero mauris varius mi, vitae suscipit ipsum ligula vitae risus. Duis aliquam nibh a dui iaculis viverra id a velit. Vivamus egestas risus in magna varius commodo.."</p>
  <div class="quote-name">-NAME HEADING</div>
</section>

<section>
  <h2 class="heading" style="top:2609px">Email Subscribe</h2>
  <p class="sub-text">Vestibulum vel metus sit amet turpis bibendum tincidunt vel sit amet quam</p>
  <div class="subscribe">
    <svg class="abs" style="left:22px;top:19px" width="18" height="14" viewBox="0 0 18 14"><rect width="18" height="14" rx="1" fill="#1b4a62"/><path d="M1 1l8 6 8-6" fill="none" stroke="#fff" stroke-width="1.5"/></svg>
    <span>Enter Email Address</span>
    <div class="btn">Sign Up</div>
  </div>
</section>

<section class="contact">
  <div class="map" role="img" aria-label="Street map showing the studio location"></div>
  <div class="form-panel">
    <h2>MAKE AN APPOINTMENT</h2>
    <div class="field" style="left:30px;top:77px;width:218px">NAME</div>
    <div class="field" style="left:266px;top:77px;width:218px">PHONE NO</div>
    <div class="field" style="left:30px;top:127px;width:218px">EMAIL ADDRESS</div>
    <div class="field" style="left:266px;top:127px;width:218px">DATE
      <svg class="abs" style="right:18px;top:13px" width="14" height="14" viewBox="0 0 14 14"><rect x="1" y="2" width="12" height="11" fill="none" stroke="#555" stroke-width="1.4"/><path d="M1 5h12M4 0v3M10 0v3" stroke="#555" stroke-width="1.4"/></svg>
    </div>
    <div class="field msg" style="left:30px;top:177px;width:454px">MESSAGE</div>
    <div class="btn submit">Submit</div>
  </div>
  <div class="contact-info">
    <div class="mark" style="left:94px;top:95px"></div>
    <h2>CONTACT US</h2>
    <div class="name">Willow Current</div>
    <div class="addr">41 Brookmere Lane, Alder Falls,<br>OR, USA, 97321</div>
    <div class="info-line" style="top:286px">
      <svg width="14" height="14" viewBox="0 0 14 14"><path d="M3 1l2.5 3-1.5 2c1 2 2 3 4 4l2-1.5 3 2.5-1.5 2C6 13 1 8 1 2.5z" fill="#1b4a62"/></svg>1-800-555-0142</div>
    <div class="info-line" style="top:312px">
      <svg width="16" height="12" viewBox="0 0 16 12"><rect width="16" height="12" rx="1" fill="#1b4a62"/><path d="M1 1l7 5 7-5" fill="none" stroke="#fff" stroke-width="1.4"/></svg>hello@willowcurrent.com</div>
    <div class="info-line" style="top:338px">
      <svg width="12" height="16" viewBox="0 0 12 16"><path d="M6 0a6 6 0 0 1 6 6c0 4-6 10-6 10S0 10 0 6a6 6 0 0 1 6-6z" fill="#1b4a62"/><circle cx="6" cy="6" r="2" fill="#fff"/></svg>Map Location</div>
  </div>
</section>

<footer>
  <div class="footer-brand"><span class="dot"></span>WILLOW CURRENT<br>MIND STUDIO</div>
  <p class="copy">Copyright © 2018. Willow Current Mind Studio. All Right Reserved</p>
  <div class="socials" aria-label="Social links"><span></span><span></span><span></span><span></span><span></span></div>
</footer>

</body>
</html>
```